Talvera Web site

Talvera is a trade name for Dresgan enterprises llc, would like Dresgan mentioned but not prominent.

Use current logo to base colors and look/feel of website. Modern trendy look.

Talvera Technical Services - "Irrevocably committed to your success"

Website design for a nation wide service based company

Networking, AV, access control, automation, EAS, project management, consulting, electrical, design, service staffing

Hostwick hosts our URL's

Questions-
Who owns the content once accepted.
How is the content delivered to build site
How do we adjust. or add to content once published

Target Market(s)

commercial and retail technical services. IE, we provide technical services for retail and commercial vertical markets

Industry/Entity Type

Trade

Coding

Coded - Design and coding required

Number of Pages Required

5+ page

Font styles to use
Sans Serif

Colors
3276b5

Requirements
Must have
• Pages-
• About/info, contact, services, customers log in portal, social media links
• links to outside web based software portals
• Call through (call me) links

```html
<!DOCTYPE html>
<html lang="en">
<head>
<meta charset="utf-8">
<title>Talvera Technical Services</title>
<link rel="stylesheet" href="https://fonts.googleapis.com/css2?family=Open+Sans:ital,wght@0,400;0,600;0,700;1,400;1,600&display=swap">
<style>
:root{
  --brand:#3276b5;
  --brand-dark:#2a63a0;
  --ink:#1d1d1d;
  --muted:#9a9a9a;
  --rule:#a9acb0;
  --panel:#f2f2f2;
  --footer:#a3a6aa;
  --white:#ffffff;
  --button-dark:#1f1b1b;
}
*{box-sizing:border-box;margin:0;padding:0}
html,body{width:1200px;height:2179px;overflow:hidden}
body{position:relative;background:var(--white);font-family:"Open Sans",sans-serif;color:var(--ink)}
.abs{position:absolute}

/* header */
.brand{left:67px;top:36px;display:flex;align-items:center;gap:12px}
.brand-mark{width:58px;height:58px;border-radius:50%;background:var(--brand)}
.brand-name{font-size:30px;font-weight:700;color:var(--brand);letter-spacing:1px}
.search{left:880px;top:46px;width:259px;height:52px;border:1.5px solid #b9bcc0;display:flex;align-items:center;padding:0 14px;font-size:16px;color:#a8a8a8;justify-content:space-between}
.nav{top:130px;font-size:16px;color:#8d8f92;letter-spacing:.3px}
.nav.active{color:var(--brand);font-weight:600}
.nav-rule{left:0;top:157px;width:1200px;height:10px;background:var(--rule)}
.nav-marker{left:413px;top:157px;width:56px;height:10px;background:var(--brand)}

/* hero */
.hero{left:23px;top:167px;width:1139px;height:539px;background:linear-gradient(120deg,#f4f4f3 0%,#e6e7e6 45%,#d9dadb 70%,#c9cbcc 100%)}
.hero-rule{left:0;top:706px;width:1200px;height:9px;background:var(--rule)}
.hero-quote{left:94px;top:237px;width:583px;height:132px;background:rgba(50,118,181,.72);color:var(--white);font-style:italic;font-weight:600;font-size:31px;line-height:44px;text-align:center;padding-top:20px}
.arrow{top:412px}

/* welcome */
.welcome-title{left:0;width:1200px;top:740px;text-align:center;font-size:28px;font-weight:600;color:#111}
.welcome-sub{left:0;width:1200px;top:782px;text-align:center;font-size:16px;font-weight:600;color:#333}
.welcome-text{left:260px;width:680px;top:811px;text-align:center;font-size:13px;line-height:22px;color:var(--muted)}

/* services */
.services{left:0;top:882px;width:1200px;height:450px;background:var(--panel)}
.services-title{left:0;width:1200px;top:905px;text-align:center;font-size:27px;font-weight:600;color:#111}
.col-rule{top:975px;width:1.5px;height:322px;background:#b6b8bb}
.svc-hex{width:72px;height:80px}
.svc-name{font-size:16px;font-weight:600;color:var(--brand)}
.svc-desc{font-size:12px;color:var(--muted);margin-top:6px}

/* about & news */
.section-title{top:1358px;font-size:27px;color:#111}
.about-photo{left:60px;top:1416px;width:329px;height:201px;background:var(--white);box-shadow:4px 6px 10px rgba(0,0,0,.28);display:flex;align-items:center;justify-content:center;gap:12px}
.about-photo .dot{width:40px;height:40px;border-radius:50%;background:var(--brand)}
.about-photo .name{font-size:34px;font-weight:600;color:var(--brand)}
.about-head{left:426px;top:1417px;font-size:16px;color:#222}
.about-sub{left:426px;top:1446px;font-size:12px;color:var(--brand)}
.about-text{left:426px;top:1478px;width:340px;font-size:13px;line-height:22px;color:var(--muted)}
.read-more{left:426px;top:1569px;width:139px;height:41px;background:var(--button-dark);color:var(--white);font-size:16px;font-weight:600;display:flex;align-items:center;justify-content:center}
.divider{left:780px;top:1366px;width:1.5px;height:254px;background:#c9cbcd}
.news-name{left:810px;top:1416px;font-size:12px;color:#222}
.news-sub{left:810px;top:1438px;font-size:13px;color:var(--brand)}
.news-quote{left:810px;top:1462px;width:185px;font-size:12px;line-height:22px;color:var(--muted);font-style:italic}
.news-photo{left:1008px;top:1418px;width:134px;height:134px;border-radius:50%;background:radial-gradient(circle at 45% 45%,#9a8c80,#5b5e62 70%,#3c3f43)}
.news-link{left:815px;top:1574px;font-size:16px;color:var(--brand);text-decoration:underline}

/* contact */
.contact{left:0;top:1659px;width:1200px;height:458px;background:var(--brand)}
.contact-title{left:0;width:1200px;top:1694px;text-align:center;font-size:27px;font-weight:600;color:var(--white);letter-spacing:.5px}
.field{border:2.5px solid #e6eef7;color:var(--white);font-size:16px;padding:12px 21px}
.submit{left:542px;top:2038px;width:116px;height:40px;background:var(--white);color:#111;font-size:16px;font-weight:700;display:flex;align-items:center;justify-content:center}

/* footer */
.footer{left:0;top:2117px;width:1200px;height:62px;background:var(--footer)}
.copyright{left:62px;top:2137px;font-size:12px;color:var(--white);font-weight:600}
.social{top:2135px;width:25px;height:25px;border-radius:4px;background:#eef0f2}
</style>
</head>
<body>

<header>
  <div class="abs brand"><span class="brand-mark"></span><span class="brand-name">TALVERA</span></div>
  <div class="abs search">search
    <svg width="20" height="20" viewBox="0 0 20 20"><circle cx="8" cy="8" r="6" fill="none" stroke="#3276b5" stroke-width="2.6"/><line x1="12.5" y1="12.5" x2="18" y2="18" stroke="#3276b5" stroke-width="3" stroke-linecap="round"/></svg>
  </div>
  <nav>
    <span class="abs nav active" style="left:417px">HOME</span>
    <span class="abs nav" style="left:502px">ABOUT US</span>
    <span class="abs nav" style="left:619px">SERVICES</span>
    <span class="abs nav" style="left:727px">CUSTOMER LOG-IN</span>
    <span class="abs nav" style="left:912px">TESTIMONIALS</span>
    <span class="abs nav" style="left:1065px">CONTACT</span>
  </nav>
  <div class="abs nav-rule"></div>
  <div class="abs nav-marker"></div>
</header>

<section>
  <div class="abs hero" role="img" aria-label="Photo of circuit breakers and a voltage tester lying on electrical blueprints"></div>
  <div class="abs hero-quote">“ IRREVOCABLY COMMITTED TO YOUR<br>SUCCESS “</div>
  <svg class="abs arrow" style="left:20px" width="22" height="36" viewBox="0 0 22 36"><polyline points="17,4 5,18 17,32" fill="none" stroke="#a9acb0" stroke-width="4"/></svg>
  <svg class="abs arrow" style="left:1156px" width="22" height="36" viewBox="0 0 22 36"><polyline points="5,4 17,18 5,32" fill="none" stroke="#a9acb0" stroke-width="4"/></svg>
  <div class="abs hero-rule"></div>
</section>

<section>
  <h1 class="abs welcome-title">WELCOME TO OUR SITE !!!</h1>
  <p class="abs welcome-sub">DEIS AUTEM VEL EUM IRIURE DOL DEIS AUTEM VEL EUM IRIURE DOL</p>
  <p class="abs welcome-text">Deis autem vel eum iriure dolor in hendrerit in vulputate velit esse molestie consequat, vel illum dolore eu feugiat nulla facilisis at vero eros et accumsan et iusto odio dignissim qui blandit praesent luptaril delenit augue duis</p>
</section>

<section>
  <div class="abs services"></div>
  <h2 class="abs services-title">OUR FEATURED SERVICES</h2>
  <div class="abs col-rule" style="left:59px"></div>
  <div class="abs col-rule" style="left:446px"></div>
  <div class="abs col-rule" style="left:814px"></div>

  <!-- column 1 -->
  <svg class="abs svc-hex" style="left:87px;top:993px" viewBox="0 0 72 80"><polygon points="36,0 72,20 72,60 36,80 0,60 0,20" fill="#3276b5"/><circle cx="36" cy="40" r="16" fill="none" stroke="#fff" stroke-width="3"/><line x1="20" y1="40" x2="52" y2="40" stroke="#fff" stroke-width="2"/></svg>
  <div class="abs" style="left:179px;top:1012px"><div class="svc-name">NETWORKING</div><div class="svc-desc">DEIS AUTEM VEL EUM IRIURE DOL</div></div>
  <svg class="abs svc-hex" style="left:87px;top:1095px" viewBox="0 0 72 80"><polygon points="36,0 72,20 72,60 36,80 0,60 0,20" fill="#3276b5"/><rect x="20" y="34" width="24" height="18" fill="#fff"/><polygon points="44,40 54,34 54,52 44,46" fill="#fff"/><circle cx="26" cy="28" r="5" fill="#fff"/><circle cx="38" cy="28" r="5" fill="#fff"/></svg>
  <div class="abs" style="left:179px;top:1114px"><div class="svc-name">AV</div><div class="svc-desc">TYPI NON HABENT T NOTARE QU</div></div>
  <svg class="abs svc-hex" style="left:87px;top:1196px" viewBox="0 0 72 80"><polygon points="36,0 72,20 72,60 36,80 0,60 0,20" fill="#3276b5"/><rect x="20" y="26" width="32" height="24" fill="none" stroke="#fff" stroke-width="3"/><line x1="25" y1="34" x2="47" y2="34" stroke="#fff" stroke-width="2"/><line x1="25" y1="40" x2="47" y2="40" stroke="#fff" stroke-width="2"/><rect x="26" y="52" width="20" height="4" fill="#fff"/></svg>
  <div class="abs" style="left:179px;top:1215px"><div class="svc-name">ACCESS CONTROL</div><div class="svc-desc">NOTARE QUAM LITTERA GO QUA</div></div>

  <!-- column 2 -->
  <svg class="abs svc-hex" style="left:475px;top:993px" viewBox="0 0 72 80"><polygon points="36,0 72,20 72,60 36,80 0,60 0,20" fill="#3276b5"/><polygon points="30,22 20,42 28,42 24,58 36,36 28,36" fill="#fff"/><text x="38" y="54" fill="#fff" font-family="Open Sans,sans-serif" font-size="20" font-weight="700">A</text></svg>
  <div class="abs" style="left:567px;top:1012px"><div class="svc-name">AUTOMATION</div><div class="svc-desc">DEIS AUTEM VEL EUM IRIURE DOL</div></div>
  <svg class="abs svc-hex" style="left:475px;top:1095px" viewBox="0 0 72 80"><polygon points="36,0 72,20 72,60 36,80 0,60 0,20" fill="#3276b5"/><path d="M20 28h12l4 4h16v22H20z" fill="#fff"/><path d="M18 54l6-18h32l-6 18z" fill="#2a63a0" stroke="#fff" stroke-width="2"/></svg>
  <div class="abs" style="left:567px;top:1114px"><div class="svc-name">PROJECT MANAGEMENT</div><div class="svc-desc">TYPI NON HABENT T NOTARE QU</div></div>
  <svg class="abs svc-hex" style="left:475px;top:1196px" viewBox="0 0 72 80"><polygon points="36,0 72,20 72,60 36,80 0,60 0,20" fill="#3276b5"/><circle cx="36" cy="26" r="6" fill="#fff"/><circle cx="25" cy="44" r="5" fill="#fff"/><circle cx="47" cy="44" r="5" fill="#fff"/><rect x="19" y="50" width="12" height="8" fill="#fff"/><rect x="41" y="50" width="12" height="8" fill="#fff"/></svg>
  <div class="abs" style="left:567px;top:1215px"><div class="svc-name">CONSULTING</div><div class="svc-desc">NOTARE QUAM LITTERA GO QUA</div></div>

  <!-- column 3 -->
  <svg class="abs svc-hex" style="left:843px;top:993px" viewBox="0 0 72 80"><polygon points="36,0 72,20 72,60 36,80 0,60 0,20" fill="#3276b5"/><rect x="28" y="30" width="16" height="20" rx="3" fill="#fff"/><line x1="18" y1="40" x2="28" y2="40" stroke="#fff" stroke-width="3"/><line x1="44" y1="34" x2="54" y2="34" stroke="#fff" stroke-width="3"/><line x1="44" y1="46" x2="54" y2="46" stroke="#fff" stroke-width="3"/></svg>
  <div class="abs" style="left:933px;top:1012px"><div class="svc-name">ELECTRICAL DESIGN</div><div class="svc-desc">DEIS AUTEM VEL EUM IRIURE DOL</div></div>
  <svg class="abs svc-hex" style="left:843px;top:1095px" viewBox="0 0 72 80"><polygon points="36,0 72,20 72,60 36,80 0,60 0,20" fill="#3276b5"/><ellipse cx="36" cy="40" rx="17" ry="13" fill="none" stroke="#fff" stroke-width="3"/><circle cx="36" cy="42" r="6" fill="#fff"/></svg>
  <div class="abs" style="left:933px;top:1114px"><div class="svc-name">EAS</div><div class="svc-desc">TYPI NON HABENT T NOTARE QU</div></div>
  <svg class="abs svc-hex" style="left:843px;top:1196px" viewBox="0 0 72 80"><polygon points="36,0 72,20 72,60 36,80 0,60 0,20" fill="#3276b5"/><circle cx="36" cy="40" r="18" fill="none" stroke="#fff" stroke-width="3"/><circle cx="36" cy="35" r="4" fill="#fff"/><circle cx="28" cy="44" r="4" fill="#fff"/><circle cx="44" cy="44" r="4" fill="#fff"/></svg>
  <div class="abs" style="left:933px;top:1215px"><div class="svc-name">SERVICE STAFFING</div><div class="svc-desc">NOTARE QUAM LITTERA GO QUA</div></div>
</section>

<section>
  <h2 class="abs section-title" style="left:61px;font-weight:400">ABOUT US</h2>
  <div class="abs about-photo"><span class="dot"></span><span class="name">DRESGAN</span></div>
  <h3 class="abs about-head" style="font-weight:400">CEIS AUTEM VEL EUM IRIURE DOLOR</h3>
  <p class="abs about-sub">DEIS AUTEM VEL EUM IRIURE DOL</p>
  <p class="abs about-text">vel illum dolore eu feugiat nulla facilisis at vero eros et accumsan et iusto odio dignissim qui blandit praesent lptaril delenit augue duis dolore</p>
  <div class="abs read-more">READ MORE</div>

  <div class="abs divider"></div>

  <h2 class="abs section-title" style="left:808px;font-weight:400">LATEST NEWS</h2>
  <p class="abs news-name">DORIAN PELLHAVEN</p>
  <p class="abs news-sub">vulputate velit esse molestie</p>
  <p class="abs news-quote">"Autem vel eum iriure dolor in hendrerit in vulputate velit esse molestie consequat, vel illum dolore eu feugiat nulla facilisis at "</p>
  <div class="abs news-photo" role="img" aria-label="Round portrait photo of the news author"></div>
  <a class="abs news-link">CONTINUE READING</a>
</section>

<section>
  <div class="abs contact"></div>
  <h2 class="abs contact-title">CONTACT FORM</h2>
  <div class="abs field" style="left:154px;top:1762px;width:254px;height:54px">NAME</div>
  <div class="abs field" style="left:471px;top:1762px;width:253px;height:54px">EMAIL</div>
  <div class="abs field" style="left:785px;top:1762px;width:253px;height:54px">PHONE</div>
  <div class="abs field" style="left:154px;top:1855px;width:885px;height:122px;padding-top:16px">MESSAGE</div>
  <div class="abs submit">SUBMIT</div>
</section>

<footer>
  <div class="abs footer"></div>
  <p class="abs copyright">Talvera Technical Services @ 2015 .All Copyrights Reserved.</p>
  <span class="abs social" style="left:998px"></span>
  <span class="abs social" style="left:1037px"></span>
  <span class="abs social" style="left:1077px"></span>
  <span class="abs social" style="left:1116px"></span>
</footer>

</body>
</html>
```